Business cards Marta Keller Sport & Events

I need new business cards to match my new logo design for my company called "Marta Keller Sport & Events". I'm based in Germany.
With my company, I offer different services in the context of sport.

Marta Keller owner

Marta Keller Sports & Events
Birkendorfer Weg 14
D-63158 Offenbach

+49 69 / 31 52 94 07
info@marta-keller-sport.example
www.marta-keller-sport.example

Contact Information for Business Card

Marta Keller Inhaberin Marta Keller Sport & Events Birkendorfer Weg 14 D-63158 Offenbach +49 69 / 31 52 94 07 info@marta-keller-sport.example www.marta-keller-sport.example

Requirements
Must have
• Logo | Double sided business card

```html
<!DOCTYPE html>
<html lang="de">
<head>
<meta charset="utf-8">
<title>Marta Keller Sport &amp; Events – Visitenkarten</title>
<link href="https://fonts.googleapis.com/css2?family=Montserrat:wght@400;500;600&display=swap" rel="stylesheet">
<style>
  :root {
    --bg: #161616;
    --card: #262626;
    --card-dark: #1f1f1f;
    --orange: #f7a21b;
    --white: #f2f2f2;
    --pattern-light: #4a4a4a;
    --pattern-dark: #2c2c2c;
  }
  * { margin: 0; padding: 0; box-sizing: border-box; }
  html, body { width: 1200px; height: 900px; overflow: hidden; }
  body {
    background: var(--bg);
    font-family: "Montserrat", sans-serif;
    position: relative;
  }
  .card {
    position: absolute;
    left: 260px;
    width: 680px;
    height: 390px;
    background: var(--card);
    border-radius: 4px;
    overflow: hidden;
    box-shadow: 0 18px 40px rgba(0,0,0,.55);
  }
  .card--back { top: 40px; background: var(--card-dark); }
  .card--front { top: 470px; }

  .pattern-field {
    position: absolute; inset: 0;
    background: linear-gradient(135deg, var(--pattern-dark) 0%, #333 55%, var(--pattern-light) 100%);
  }
  .brand {
    position: absolute;
    display: flex; align-items: center; gap: 12px;
  }
  .brand__dot {
    border-radius: 50%;
    background: var(--orange);
    flex: none;
  }
  .brand__name {
    font-weight: 600;
    letter-spacing: .08em;
    text-transform: uppercase;
    color: var(--white);
  }
  .card--back .brand { right: 40px; bottom: 70px; }
  .card--back .brand__dot { width: 38px; height: 38px; }
  .card--back .brand__name { font-size: 13px; }

  .card--front .brand { left: 40px; top: 40px; }
  .card--front .brand__dot { width: 56px; height: 56px; }
  .card--front .brand__name { font-size: 17px; }

  .address {
    position: absolute; left: 78px; top: 150px;
    font-size: 17px; line-height: 1.3; color: var(--white);
  }
  .address__company { color: var(--orange); }

  .contact {
    position: absolute; left: 56px; top: 245px;
    list-style: none; font-size: 17px; color: var(--white);
  }
  .contact li { display: flex; align-items: center; gap: 12px; line-height: 1.55; }
  .contact svg { width: 14px; height: 14px; flex: none; }

  .mark-field {
    position: absolute; right: -40px; top: 120px;
    width: 340px; height: 340px; border-radius: 50%;
    background: radial-gradient(circle, #2f2f2f 0%, #2b2b2b 60%, rgba(38,38,38,0) 72%);
  }
  .person {
    position: absolute; right: 60px; top: 175px; text-align: right;
  }
  .person__name { color: var(--orange); font-size: 24px; font-weight: 500; letter-spacing: .01em; }
  .person__role { color: var(--white); font-size: 19px; }
  .accent-bar {
    position: absolute; right: 20px; top: 192px;
    width: 24px; height: 48px; background: var(--orange);
  }
</style>
</head>
<body>

<section class="card card--back" aria-label="Rückseite">
  <div class="pattern-field" role="img" aria-label="Geprägtes Wiederholungsmuster aus dem Firmenzeichen"></div>
  <div class="brand">
    <span class="brand__dot"></span>
    <span class="brand__name">Marta Keller Sport &amp; Events</span>
  </div>
</section>

<section class="card card--front" aria-label="Vorderseite">
  <div class="brand">
    <span class="brand__dot"></span>
    <span class="brand__name">Marta Keller Sport &amp; Events</span>
  </div>

  <address class="address" style="font-style:normal">
    <div class="address__company">Marta Keller Sports &amp; Events</div>
    <div>Birkendorfer Weg 14</div>
    <div>D-63158 Offenbach</div>
  </address>

  <ul class="contact">
    <li>
      <svg viewBox="0 0 14 14"><path d="M3 1h3l1 3-2 1.2c.8 1.7 2 2.9 3.8 3.8L10 7l3 1v3c0 1-1 2-2 2C5.5 13 1 8.5 1 3c0-1 1-2 2-2z" fill="var(--orange)"/></svg>
      +49 69 / 31 52 94 07
    </li>
    <li>
      <svg viewBox="0 0 14 14"><rect x="1" y="3" width="12" height="8" fill="none" stroke="var(--orange)" stroke-width="1.4"/><path d="M1 3l6 5 6-5" fill="none" stroke="var(--orange)" stroke-width="1.4"/></svg>
      info@marta-keller-sport.example
    </li>
    <li>
      <svg viewBox="0 0 14 14"><circle cx="7" cy="7" r="6" fill="none" stroke="var(--orange)" stroke-width="1.3"/><ellipse cx="7" cy="7" rx="2.6" ry="6" fill="none" stroke="var(--orange)" stroke-width="1.1"/><path d="M1 7h12M2 4h10M2 10h10" stroke="var(--orange)" stroke-width="1"/></svg>
      www.marta-keller-sport.example
    </li>
  </ul>

  <div class="mark-field" role="img" aria-label="Großes, dezentes Firmenzeichen als Hintergrund"></div>

  <div class="person">
    <div class="person__name">MARTA KELLER</div>
    <div class="person__role">owner</div>
  </div>
  <div class="accent-bar"></div>
</section>

</body>
</html>
```